Financial Advisor / Asset Manager Zup Design

I'm currently hosting with Zup and my first attempt at a website is live at www.ravenholtwealth.example Clearly I am not a web designer and I need help making this more catchy, modern, cross-platform compatible, search engine optimized, etc. I've got logos, hex color pallets, and a slew of other graphics. I'm interested in working with a winning designer to write/refine my copy/language to complete the build.

Full set of graphics https://pics.lumora-share.example/q71TzR05KwPd2MhXN do NOT use the CONSULTING graphics as this is for a related business / different website

Target Market(s)

Individuals, small institutions, endowments, non-profits seeking financial advice and asset / portfolio management

Industry/Entity Type

Financial Services

Coding

Coded - Design and coding required

Font styles to use
Other font styles liked:
• AvenirLTStd - Black, Book, and Roman as appropriate

Requirements
Must have
• Complete, cross platform website integrating my existing logo
Nice to have
• Easy to update format for go-forward maintenance

```html
<!DOCTYPE html>
<html lang="en">
<head>
<meta charset="utf-8">
<title>Ravenholt Capital — Financial Advice &amp; Asset Management</title>
<link href="https://fonts.googleapis.com/css2?family=Nunito+Sans:wght@300;400;600;700;800;900&family=Catamaran:wght@500;600;700&display=swap" rel="stylesheet">
<style>
:root{
  --blue:#1a7ccc;
  --blue-light:#4a9ad8;
  --cyan:#07a9e8;
  --navy:#0f2a52;
  --navy-deep:#0a1f40;
  --ink:#333a44;
  --muted:#555c66;
  --grey-bg:#f4f4f4;
  --steel:#6b97b8;
  --white:#ffffff;
  --black:#0b0b0b;
}
*{box-sizing:border-box;margin:0;padding:0}
html,body{width:1200px;height:3322px;overflow:hidden}
body{font-family:"Nunito Sans",sans-serif;color:var(--ink);background:var(--white);position:relative}
.abs{position:absolute}
.btn{position:absolute;z-index:3;display:flex;align-items:center;justify-content:space-between;width:182px;height:48px;padding:0 14px 0 20px;background:var(--blue);color:var(--white);font-weight:700;font-size:14px;letter-spacing:.5px;border-radius:3px;text-decoration:none}
.btn .arrow{width:32px;height:32px;border-radius:50%;background:var(--white);display:flex;align-items:center;justify-content:center}

/* hero */
.hero{position:absolute;left:0;top:0;width:1200px;height:703px;background:linear-gradient(180deg,#3a6aa8 0%,#8fb0d6 25%,#5d7fae 45%,#b9cbe3 65%,#eef3f9 85%,#ffffff 100%)}
.nav{position:absolute;top:0;left:0;width:1200px;height:84px}
.brand{position:absolute;left:115px;top:28px;display:flex;align-items:center;gap:10px;color:var(--white);font-size:22px;font-weight:600;letter-spacing:1px}
.brand .dot{width:16px;height:16px;border:2px solid var(--white);border-radius:50%}
.menu{position:absolute;left:453px;top:34px;display:flex;gap:40px;list-style:none}
.menu a{color:var(--white);font-size:14px;text-decoration:none;font-weight:600}
.menu .active{font-weight:800;border-bottom:3px solid var(--white);padding-bottom:8px}
.call{position:absolute;left:866px;top:14px;width:222px;height:56px;border-radius:6px;background:rgba(120,180,230,.75);color:var(--white);font-weight:800;font-size:17px;display:flex;align-items:center;gap:14px;padding-left:16px}
.call .ring{width:40px;height:40px;border:2px solid var(--white);border-radius:50%;display:flex;align-items:center;justify-content:center}
.hero-panel{position:absolute;left:0;top:231px;width:626px;height:293px;background:rgba(70,80,100,.55)}
.hero-panel h1{position:absolute;left:111px;font-family:"Catamaran",sans-serif;font-weight:600;font-size:32px;line-height:39px;color:var(--white);text-shadow:0 2px 4px rgba(0,0,0,.4)}
.slide-arrow{position:absolute;top:352px;width:58px;height:58px;border:1px solid rgba(255,255,255,.5);border-radius:50%;display:flex;align-items:center;justify-content:center}
.dots{position:absolute;top:662px;left:540px;display:flex;gap:10px}
.dots span{width:20px;height:3px;background:#222}
.dots .on{width:34px;background:var(--blue)}

h2.title{font-size:38px;font-weight:800;color:var(--ink);font-family:"Nunito Sans",sans-serif}
h2.title span{font-weight:300}
.bar{width:50px;height:4px;background:var(--blue);margin-top:10px}

/* about */
.about-text{position:absolute;left:671px;top:775px;width:422px}
.about-text p{margin-top:22px;font-size:15.5px;line-height:25.8px;text-align:justify;color:var(--muted)}

/* services */
.services{position:absolute;left:0;top:1181px;width:1200px;height:585px;background:var(--grey-bg)}
.services .head{position:absolute;top:70px;width:1200px;text-align:center}
.services .head .bar{margin:10px auto 0}
.card{position:absolute;top:177px;width:311px;height:322px;background:var(--white);box-shadow:0 4px 10px rgba(0,0,0,.12);border-radius:4px}
.card .tri{position:absolute;left:-48px;top:20px}
.card h3{position:absolute;left:87px;font-family:"Catamaran",sans-serif;font-size:26px;font-weight:600;line-height:30px;color:var(--ink)}
.card p{position:absolute;left:87px;width:210px;font-size:12.4px;line-height:20.6px;color:var(--muted)}
.card .more{position:absolute;left:87px;top:262px;display:flex;align-items:center;gap:12px;font-size:14px;font-style:italic;text-decoration:underline;color:var(--ink)}
.card .more i{display:block;width:34px;height:20px;position:relative}

/* faq */
.faq{position:absolute;left:0;top:1766px;width:1200px;height:725px;background:linear-gradient(135deg,#1c3f70 0%,var(--navy) 45%,var(--navy-deep) 100%)}
.faq h2{position:absolute;top:74px;width:1200px;text-align:center;font-family:"Catamaran",sans-serif;color:var(--white);font-size:40px;font-weight:700}
.faq .underline{position:absolute;top:130px;left:575px;width:50px;height:4px;background:var(--white)}
.q{position:absolute;left:262px;width:676px;height:42px;border-radius:21px;background:var(--white);display:flex;align-items:center;font-size:13px;color:var(--ink)}
.q .sign{width:26px;height:26px;margin:0 22px 0 10px;border:1px solid var(--blue);border-radius:50%;display:flex;align-items:center;justify-content:center;color:var(--blue);font-size:14px}
.q.open{background:var(--cyan);color:var(--white)}
.q.open .sign{background:var(--navy);border-color:var(--navy);color:var(--white)}
.answer{position:absolute;left:324px;top:2058px;width:584px;color:var(--white);font-size:11px;line-height:19.6px;text-align:justify}

/* contact */
.touch{position:absolute;left:0;top:2491px;width:601px;height:521px;background:#f7f9fb}
.reach{position:absolute;left:601px;top:2491px;width:599px;height:521px;background:var(--steel)}
.field{position:absolute;height:38px;border:1px solid var(--blue-light);background:var(--white);font-size:10px;color:var(--muted);padding:12px 16px}
.scenery{position:absolute;left:0;top:2932px;width:1200px;height:80px;background:linear-gradient(180deg,rgba(200,208,218,0) 0%,rgba(170,180,192,.7) 55%,#7d8692 100%)}
.info{position:absolute;left:676px;display:flex;gap:12px;color:var(--white)}
.info .ico{width:52px;height:52px;border:1px solid rgba(255,255,255,.8);border-radius:50%;display:flex;align-items:center;justify-content:center}
.info b{display:block;font-size:13px;font-weight:800;margin-top:5px}
.info span{font-size:13px;line-height:20px}

/* footer */
.footer{position:absolute;left:0;top:3012px;width:1200px;height:310px;background:var(--black);color:var(--white);text-align:center}
.footer .brand{position:static;justify-content:center;margin-top:60px;font-size:18px}
.footer ul{display:flex;justify-content:center;gap:40px;list-style:none;margin-top:22px;font-size:13.5px;font-weight:600}
.footer .rule{width:976px;height:1px;background:var(--blue);margin:0 auto}
.footer .legal{font-size:12px;line-height:20px;padding:20px 0}
.footer .copy{font-size:13px;font-weight:600;margin-top:24px}
</style>
</head>
<body>

<header class="hero">
  <div role="img" aria-label="Snow-covered mountain range under a blue sky" class="abs" style="inset:0"></div>
  <nav class="nav">
    <div class="brand"><span class="dot"></span>RAVENHOLT CAPITAL</div>
    <ul class="menu">
      <li><a class="active" href="#">Home</a></li>
      <li><a href="#">About</a></li>
      <li><a href="#">FAQs</a></li>
      <li><a href="#">Services</a></li>
      <li><a href="#">Contact</a></li>
    </ul>
    <div class="call"><span class="ring"><svg width="18" height="18" viewBox="0 0 24 24" fill="none" stroke="#fff" stroke-width="2"><path d="M5 3h4l2 5-3 2a12 12 0 006 6l2-3 5 2v4a2 2 0 01-2 2A18 18 0 013 5a2 2 0 012-2z"/></svg></span>(555) 014-2290</div>
  </nav>
  <div class="hero-panel">
    <h1 style="top:20px">Personalized financial advice<br>to help you achieve your goals</h1>
    <h1 style="top:116px">Professional management to<br>make your money work for you</h1>
  </div>
  <a class="btn" style="left:113px;top:452px" href="#">LEARN MORE<span class="arrow"><svg width="14" height="12" viewBox="0 0 14 12" fill="none" stroke="#1a7ccc" stroke-width="1.6"><path d="M0 6h12M7 1l5 5-5 5"/></svg></span></a>
  <div class="slide-arrow" style="left:24px"><svg width="18" height="14" viewBox="0 0 18 14" fill="none" stroke="#fff" stroke-width="1.6"><path d="M18 7H2M7 1L1 7l6 6"/></svg></div>
  <div class="slide-arrow" style="left:1118px"><svg width="18" height="14" viewBox="0 0 18 14" fill="none" stroke="#fff" stroke-width="1.6"><path d="M0 7h16M11 1l6 6-6 6"/></svg></div>
  <div class="dots"><span class="on"></span><span></span><span></span><span></span></div>
</header>

<section class="about">
  <svg class="abs" style="left:85px;top:765px" width="560" height="305" viewBox="0 0 560 305" role="img" aria-label="Photo of a couple reviewing financial paperwork, framed in triangular peak shapes">
    <defs><linearGradient id="photo" x1="0" y1="0" x2="1" y2="0"><stop offset="0" stop-color="#e6e2de"/><stop offset=".5" stop-color="#cdbfb2"/><stop offset="1" stop-color="#dfe4ea"/></linearGradient></defs>
    <polygon points="0,258 141,35 195,108 287,0 330,62 280,258" fill="url(#photo)"/>
    <polygon points="262,290 402,43 555,288" fill="url(#photo)"/>
    <rect x="0" y="258" width="280" height="8" fill="#4a9ad8"/>
    <rect x="260" y="288" width="296" height="9" fill="#4a9ad8"/>
  </svg>
  <div class="about-text">
    <h2 class="title">Who <span>We Are</span></h2>
    <div class="bar"></div>
    <p>Ravenholt Capital is a registered investment advisory firm committed to serving as fiduciary to our clients. We always act in the best interests of our clients, including putting your interests ahead of our own. We provide independent financial planning, investment management, and asset management services tailored to your unique needs and circumstances.</p>
  </div>
  <a class="btn" style="left:671px;top:1048px" href="#">LEARN MORE<span class="arrow"><svg width="14" height="12" viewBox="0 0 14 12" fill="none" stroke="#1a7ccc" stroke-width="1.6"><path d="M0 6h12M7 1l5 5-5 5"/></svg></span></a>
</section>

<section class="services">
  <div class="head"><h2 class="title">Services <span>We Offer</span></h2><div class="bar"></div></div>

  <article class="card" style="left:93px">
    <svg class="tri" width="146" height="124" viewBox="0 0 146 124"><polygon points="0,0 146,0 73,124" fill="#4a9ad8"/><g fill="none" stroke="#fff" stroke-width="2"><rect x="48" y="40" width="6" height="18"/><rect x="60" y="32" width="6" height="26"/><rect x="72" y="36" width="6" height="22"/><rect x="84" y="28" width="6" height="30"/><circle cx="60" cy="20" r="7"/></g></svg>
    <h3 style="top:40px">Stock Screening</h3>
    <p style="top:90px">Many advisors use a screening process to find investments. You may be familiar with stock screening as many websites and investment platforms (like Brokerline) make screening tools available for free.</p>
    <a class="more" href="#">Learn More <i><svg width="34" height="20" viewBox="0 0 34 20"><rect width="20" height="20" rx="3" fill="#1a7ccc"/><path d="M8 10h24M27 5l5 5-5 5" stroke="#222" stroke-width="1.8" fill="none"/></svg></i></a>
  </article>

  <article class="card" style="left:469px">
    <svg class="tri" width="146" height="124" viewBox="0 0 146 124"><polygon points="0,0 146,0 73,124" fill="#4a9ad8"/><g fill="none" stroke="#fff" stroke-width="2"><path d="M70 66V42l18-14M80 26h9v9M70 48l-14-10M56 32v8h8"/></g></svg>
    <h3 style="top:28px">Alternative<br>Investments</h3>
    <p style="top:88px">The challenges facing investors seeking to build portfolios capable of generating attractive returns with acceptable levels of risk may never have been greater. The traditional 60% stock / 40% bond portfolio mix that has worked effectively for many years needs</p>
    <a class="more" href="#">Learn More <i><svg width="34" height="20" viewBox="0 0 34 20"><rect width="20" height="20" rx="3" fill="#1a7ccc"/><path d="M8 10h24M27 5l5 5-5 5" stroke="#222" stroke-width="1.8" fill="none"/></svg></i></a>
  </article>

  <article class="card" style="left:844px">
    <svg class="tri" width="146" height="124" viewBox="0 0 146 124"><polygon points="0,0 146,0 73,124" fill="#4a9ad8"/><g fill="none" stroke="#fff" stroke-width="2"><circle cx="73" cy="40" r="24" stroke-dasharray="5 3"/><circle cx="73" cy="40" r="16"/><path d="M66 46v-6M71 46v-10M76 46v-8M81 46v-12"/></g></svg>
    <h3 style="top:40px">Optimization</h3>
    <p style="top:90px">Your investment portfolio was built with money you earned. It should be customized to reflect your goals and tailored to help you meet your financial needs. ETFs and mutual funds are generally passive and impersonal - the fund manager doesn't know</p>
    <a class="more" href="#">Learn More <i><svg width="34" height="20" viewBox="0 0 34 20"><rect width="20" height="20" rx="3" fill="#1a7ccc"/><path d="M8 10h24M27 5l5 5-5 5" stroke="#222" stroke-width="1.8" fill="none"/></svg></i></a>
  </article>
</section>

<section class="faq" role="img" aria-label="Dark blue background of stock market charts and figures">
  <h2>Frequently Asked Questions (FAQs)</h2>
  <div class="underline"></div>
</section>
<div class="q" style="top:1932px"><span class="sign">+</span>What is a registered investment advisor? Are you a registered investment advisor?</div>
<div class="q open" style="top:1994px"><span class="sign">-</span>What are your fees? How much will I pay?</div>
<p class="answer">We charge fees based on the services being provided. For the most part, we actively manage our clients' portfolios and charge fees as a percentage of assets under management (AUM). For clients whose situations are not well suited for asset management strategies, we charge a flat or per hour fee for consulting or advisory services. We always disclose our fees upfront, so you will always know what you pay and how we get paid.</p>
<div class="q" style="top:2153px"><span class="sign">+</span>What is a fiduciary? Are you a fiduciary?</div>
<div class="q" style="top:2222px"><span class="sign">+</span>What is a custodian? Are you a custodian?</div>
<div class="q" style="top:2290px"><span class="sign">+</span>How often will we meet? How will you keep me informed?</div>
<a class="btn" style="left:524px;top:2358px" href="#">VIEW MORE<span class="arrow"><svg width="14" height="12" viewBox="0 0 14 12" fill="none" stroke="#1a7ccc" stroke-width="1.6"><path d="M0 6h12M7 1l5 5-5 5"/></svg></span></a>

<section class="touch">
  <div class="abs" style="left:113px;top:75px"><h2 class="title">Get In <span>Touch</span></h2><div class="bar"></div></div>
</section>
<section class="reach">
  <div class="abs" style="left:75px;top:75px"><h2 class="title" style="color:#fff">Contact <span>Us</span></h2><div class="bar" style="background:#fff"></div></div>
</section>
<div class="scenery" role="img" aria-label="Snowy mountain scenery along the bottom edge"></div>

<div class="field" style="left:113px;top:2647px;width:204px">Your Name*</div>
<div class="field" style="left:331px;top:2647px;width:204px">Last Name*</div>
<div class="field" style="left:113px;top:2699px;width:204px">Email*</div>
<div class="field" style="left:331px;top:2699px;width:204px">Phone*</div>
<div class="field" style="left:113px;top:2751px;width:422px;height:108px">Leave us a message*</div>
<a class="btn" style="left:113px;top:2878px;width:132px" href="#">SUBMIT<span class="arrow"><svg width="14" height="12" viewBox="0 0 14 12" fill="none" stroke="#1a7ccc" stroke-width="1.6"><path d="M0 6h12M7 1l5 5-5 5"/></svg></span></a>

<div class="info" style="top:2648px"><span class="ico"><svg width="18" height="24" viewBox="0 0 18 24" fill="#fff"><path d="M9 0a9 9 0 00-9 9c0 7 9 15 9 15s9-8 9-15a9 9 0 00-9-9zm0 12a3 3 0 110-6 3 3 0 010 6z"/></svg></span><div><b>ADDRESS</b><span>208 Alder Ridge Rd, Suite #40<br>Maplefield, VA 20199</span></div></div>
<div class="info" style="top:2732px"><span class="ico"><svg width="20" height="20" viewBox="0 0 24 24" fill="none" stroke="#fff" stroke-width="2"><path d="M5 3h4l2 5-3 2a12 12 0 006 6l2-3 5 2v4a2 2 0 01-2 2A18 18 0 013 5a2 2 0 012-2z"/></svg></span><div><b>PHONE</b><span>(555) 014-2290</span></div></div>
<div class="info" style="top:2810px"><span class="ico"><svg width="22" height="16" viewBox="0 0 22 16" fill="none" stroke="#fff" stroke-width="2"><rect x="1" y="1" width="20" height="14"/><path d="M1 1l10 8 10-8"/></svg></span><div><b>EMAIL</b><span>hello@ravenholtwealth.example</span></div></div>

<footer class="footer">
  <div class="brand"><span class="dot"></span>RAVENHOLT CAPITAL</div>
  <ul><li>Home</li><li>About</li><li>FAQs</li><li>Services</li><li>Contact</li></ul>
  <div class="rule" style="margin-top:22px"></div>
  <p class="legal">Ravenholt Capital LLC ® is a Registered Investment Advisor CRD #482106. We proudly serve as fiduciary to our clients and support our local communities.<br>Ravenholt Capital is carbon neutral with the help of greenoffset.example</p>
  <div class="rule"></div>
  <p class="copy">© COPYRIGHT 2022 | ALL RIGHTS RESERVED</p>
</footer>

</body>
</html>
```